Professional Website for Brightfold Laundry Company

Brightfold Laundry Company is a family-owned laundry service provider that has been serving Midtown Atlanta for over 45 years. We provide express clothing and linen washing services to residential and commercial clients in Atlanta and surrounding areas.

The final website and logo design should convey professionalism and give the customer a sense of security in having their personal items laundered with us.

Target Market(s)

Commercial Businesses and high net worth personal customers

Industry/Entity Type

Professional Laundry Services

Coding

Coded - Design and coding required

Number of Pages Required

5+ page

Font styles to use
Sans Serif

Colors
0054AA
0677BA
7BADD7
CADEEF
E8F1F8

Requirements
Must have
• I would like to have the following elements on my website: 1. Blog page 2. Contact Us Form 3. Sign up for service (sample attached) 4. Sections outlined in the content copy page 5. Links to social media accounts.
Nice to have
• A great example is https://www.quillmarsh.example/laundry-pick-up-and-delivery/?utm_term=pick%20up%20and%20delivery%20laundry%20service&utm_campaign=*QM%20United%20States%20%7C%20Search%20(Broad%20KWs)&utm_source=zorvik&utm_medium=ppc&hsa_acc=1111111111&hsa_cam=22222222222&hsa_grp=3333333333333333&hsa_ad=&hsa_src=o&hsa_tgt=kwd-44444444444444:loc-100&hsa_kw=pick%20up%20and%20delivery%20laundry%20service&hsa_mt=e&hsa_net=zorvik&hsa_ver=3&msclkid=00000000000000000000000000000000

```html
<!DOCTYPE html>
<html lang="en">
<head>
<meta charset="utf-8">
<title>Brightfold Laundry Company</title>
<link rel="stylesheet" href="https://fonts.googleapis.com/css2?family=Poppins:wght@400;500;600;700&display=swap">
<style>
:root{
  --navy:#00468c;
  --primary:#0054aa;
  --accent:#0677ba;
  --sky:#7badd7;
  --pale:#cadeef;
  --mist:#e8f1f8;
  --faint:#f5f8fc;
  --ink:#111;
  --grey:#6b6b6b;
  --white:#fff;
  --black:#000;
}
*{box-sizing:border-box;margin:0;padding:0}
html,body{width:1200px;height:3177px;overflow:hidden}
body{position:relative;font-family:"Poppins",sans-serif;color:var(--ink);background:var(--white)}
.abs{position:absolute}
.hero-bg{left:0;top:0;width:1200px;height:660px}
.topbar{top:8px;right:62px;display:flex;gap:36px;color:var(--white);font-size:12px;font-weight:500;align-items:center}
.topbar span{display:flex;align-items:center;gap:10px}
.nav{left:60px;top:34px;width:1080px;height:58px;background:var(--white);border-radius:4px;display:flex;align-items:center;padding:0 20px}
.brand{font-weight:600;font-size:17px;line-height:1.1;color:var(--ink)}
.nav-links{display:flex;gap:32px;margin-left:auto;margin-right:30px;font-size:13px}
.nav-links .active{border-bottom:2px solid var(--accent);padding-bottom:3px}
.btn{display:inline-flex;align-items:center;justify-content:center;border-radius:20px;font-size:13px}
.btn-blue{background:var(--primary);color:var(--white)}
.btn-white{background:var(--white);color:var(--ink)}
.hero-title{left:62px;top:190px;font-size:42px;font-weight:600;line-height:1.18;color:var(--white)}
.hero-text{left:62px;top:300px;width:475px;font-size:13px;line-height:21px;color:var(--white)}
.ph{border-radius:50%}
h2{font-size:27px;font-weight:600}
h2 em{font-style:normal;color:var(--primary)}
.underline::after{content:"";display:block;width:82px;height:2px;background:var(--accent);margin-top:4px}
.body-text{font-size:13.5px;line-height:22.5px;color:var(--grey)}
.svc{font-size:14px;font-weight:500;display:flex;align-items:center;gap:14px}
.icon-dot{width:60px;height:60px;border-radius:50%;background:var(--accent);border:3px solid var(--pale);display:flex;align-items:center;justify-content:center}
.icon-dot i{width:26px;height:26px;border:2px solid var(--white);border-radius:6px}
.step{width:320px;text-align:center}
.step h3{font-size:17px;font-weight:500;margin:0 0 8px}
.step p{font-size:13px;line-height:22px;color:var(--grey)}
.arrow{width:36px;height:36px;border-radius:50%;display:flex;align-items:center;justify-content:center}
.footer-col h4{font-size:13px;font-weight:400;color:var(--accent);margin-bottom:14px}
.footer-col li{list-style:none;font-size:12px;color:var(--white);margin-bottom:16px}
.contact-row{display:flex;gap:14px;font-size:12px;color:var(--white);margin-bottom:20px;line-height:18px}
.social{width:30px;height:30px;border-radius:50%}
</style>
</head>
<body>

<svg class="abs hero-bg" viewBox="0 0 1200 660" aria-hidden="true">
  <path d="M0 0H1200V545C1120 585 1040 630 920 612C780 590 640 600 480 632C330 662 200 600 120 608C60 614 20 630 0 640Z" fill="var(--accent)"/>
  <path d="M0 0H1200V548C1120 590 1050 618 920 600C780 580 640 600 480 630C330 660 200 590 120 600C60 606 20 618 0 628Z" fill="var(--navy)"/>
</svg>

<div class="abs topbar">
  <span><svg width="14" height="14" viewBox="0 0 24 24"><path d="M6.6 10.8a15 15 0 0 0 6.6 6.6l2.2-2.2c.3-.3.7-.4 1-.2 1.1.4 2.3.6 3.6.6.6 0 1 .4 1 1V20c0 .6-.4 1-1 1A17 17 0 0 1 3 4c0-.6.4-1 1-1h3.5c.6 0 1 .4 1 1 0 1.3.2 2.5.6 3.6.1.3 0 .7-.2 1z" fill="#fff"/></svg>404-555-0142</span>
  <span><svg width="18" height="13" viewBox="0 0 18 13"><rect width="18" height="13" fill="#fff"/><path d="M0 0l9 7 9-7" stroke="#00468c" fill="none"/></svg>info@brightfoldlaundry.example</span>
</div>

<nav class="abs nav">
  <div class="brand">Brightfold Laundry<br>Company</div>
  <div class="nav-links"><span class="active">Home</span><span>About</span><span>Services</span><span>Why Choose Us</span><span>Blog</span><span>Contact Us</span><span>Log In</span></div>
  <a class="btn btn-blue" style="width:132px;height:36px">Sign Up Today</a>
</nav>

<h1 class="abs hero-title">washing &amp; Dry Cleaning<br>Laundary Service</h1>
<p class="abs hero-text">We are proud to offer high quality and convenient services to the area residents and business owners and strive to keep our customers' clothing in tip top shape.</p>
<a class="abs btn btn-white" style="left:60px;top:423px;width:142px;height:36px">Let's Get Started</a>
<div class="abs ph" role="img" aria-label="Woman holding a phone and a stack of folded jeans" style="left:740px;top:173px;width:358px;height:358px;background:radial-gradient(circle at 50% 45%,#8a7a5a 0 30%,var(--accent) 31%);border:4px solid #0a63b0"></div>

<div class="abs" role="img" aria-label="Woman loading a front-loading washing machine" style="left:60px;top:697px;width:304px;height:275px;border-radius:6px;background:linear-gradient(135deg,#e9e3d6,#c9b79a)"></div>
<div class="abs" style="left:308px;top:876px;width:112px;height:112px;border-radius:50%;background:var(--primary);border:3px solid var(--white);color:var(--white);text-align:center;padding-top:18px">
  <div style="font-size:20px;font-weight:600;line-height:1.2">45<br>Years</div>
  <div style="font-size:10px">Service Provide</div>
</div>
<h2 class="abs underline" style="left:538px;top:688px">Welcome To <em>Brightfold Laundry</em></h2>
<p class="abs body-text" style="left:538px;top:746px;width:575px">Brightfold Laundry Company is a family-owned laundry service provider that has been serving Midtown Atlanta for over 45 years. We are proud to offer high quality and convenient services to the area residents and business owners and strive to keep our customers' clothing in tip top shape.</p>
<p class="abs body-text" style="left:537px;top:847px;width:575px">Whether you have commercial laundry needs, are washing clothes for your family, or want to relax that weekend and have us pick up and wash/dry/fold for you, the professionals at Brightfold Laundry Company.</p>
<a class="abs btn btn-blue" style="left:535px;top:947px;width:108px;height:36px">Read More</a>

<svg class="abs" style="left:0;top:1060px" width="1200" height="545" viewBox="0 0 1200 545" aria-hidden="true">
  <path d="M0 20C120 -10 220 20 320 10C450 0 520 45 700 40C880 35 1000 0 1100 40C1150 60 1180 80 1200 100V545H0Z" fill="var(--mist)"/>
</svg>
<h2 class="abs" style="left:0;width:1200px;top:1198px;text-align:center">Our <em>Services</em><span style="display:block;width:82px;height:2px;background:var(--accent);margin:4px 0 0 516px"></span></h2>
<div class="abs ph" role="img" aria-label="Woman holding a basket of laundry" style="left:470px;top:1298px;width:260px;height:260px;background:radial-gradient(circle at 50% 50%,#f0c85a 0 25%,#1f8fe0 26%);border:4px solid #4fa7e8"></div>

<div class="abs svc" style="right:791px;top:1276px">Commercial Services<div class="icon-dot"><i></i></div></div>
<div class="abs svc" style="right:805px;top:1378px">Light Commercial Services<div class="icon-dot"><i></i></div></div>
<div class="abs svc" style="right:805px;top:1476px">Wash Dry Fold<div class="icon-dot"><i></i></div></div>
<div class="abs svc" style="left:767px;top:1290px"><div class="icon-dot"><i></i></div>Professional Laundry Services</div>
<div class="abs svc" style="left:783px;top:1378px"><div class="icon-dot"><i></i></div>Pickup and Delivery</div>
<div class="abs svc" style="left:779px;top:1476px"><div class="icon-dot"><i></i></div>Dry Cleaning</div>

<h2 class="abs" style="left:0;width:1200px;top:1677px;text-align:center">How We <em>Work</em><span style="display:block;width:82px;height:2px;background:var(--accent);margin:4px 0 0 510px"></span></h2>
<div class="abs" role="img" aria-label="Person seated beside a large phone showing a sign-up screen" style="left:190px;top:1745px;width:130px;height:136px;border-radius:50%;background:linear-gradient(#e4ebf3,#cfdbe8)"></div>
<div class="abs" role="img" aria-label="Washing machine with detergent bottles" style="left:525px;top:1745px;width:160px;height:136px;border-radius:50%;background:linear-gradient(#e4ebf3,#cfdbe8)"></div>
<div class="abs" role="img" aria-label="Hand holding a phone next to a delivery van and location marker" style="left:850px;top:1745px;width:215px;height:136px;border-radius:12px;background:linear-gradient(#e4ebf3,#8fb5dc)"></div>
<div class="abs step" style="left:93px;top:1890px"><h3>Sign Up</h3><p>Give us a call at 404-555-0142 or use our sign up page to schedule service. You can control the frequency of how often we process your laundry.</p></div>
<div class="abs step" style="left:442px;top:1890px"><h3>Fill Out a Customer Profile</h3><p>When setting up your customer profile you can detail how you want your laundry processed; hangers for shirts, pants folded, etc. You can select your laundry detergents, bleaches and softeners from a list of provided products.</p></div>
<div class="abs step" style="left:797px;top:1890px"><h3>Schedule a Pickup</h3><p>Place your clothes in the Brightfold Laundry Company bag and leave it out on your scheduled pickup day. We will process your clothing as instructed and deliver it back to your doorstep within 24 hours.</p></div>

<svg class="abs" style="left:0;top:2085px" width="1200" height="387" viewBox="0 0 1200 387" aria-hidden="true">
  <path d="M0 5C150 -10 260 40 420 45C600 50 700 0 880 20C1020 35 1120 50 1200 40V387H0Z" fill="var(--faint)"/>
</svg>
<h2 class="abs" style="left:0;width:1200px;top:2217px;text-align:center">What Our <em>Customer Says...</em><span style="display:block;width:112px;height:2px;background:var(--accent);margin:4px 0 0 425px"></span></h2>
<div class="abs" style="left:579px;top:2281px;width:48px;height:48px;border-radius:50%;background:var(--mist);display:flex;align-items:center;justify-content:center;color:var(--accent);font-size:38px;font-weight:700;line-height:1;padding-top:14px">&ldquo;</div>
<p class="abs body-text" style="left:325px;top:2340px;width:558px;text-align:center">Lorem Ipsum is simply dummy text of the printing and typesetting industry. Lorem Ipsum has been the industry's standard dummy text ever since the 1500s, when an unknown printer took a galley of type and scrambled it to make a type specimen book.</p>
<div class="abs arrow" style="left:161px;top:2340px;background:var(--accent)"><svg width="12" height="12" viewBox="0 0 12 12"><path d="M8 1L3 6l5 5" stroke="#fff" stroke-width="1.6" fill="none"/></svg></div>
<div class="abs arrow" style="left:990px;top:2340px;background:var(--pale)"><svg width="12" height="12" viewBox="0 0 12 12"><path d="M4 1l5 5-5 5" stroke="#333" stroke-width="1.6" fill="none"/></svg></div>

<h2 class="abs" style="left:0;width:1200px;top:2517px;text-align:center">Ready To Start?</h2>
<p class="abs body-text" style="left:380px;top:2562px;width:440px;text-align:center">Give us a call at <u>404-555-0142</u> or use our sign up page to schedule service.</p>
<a class="abs btn btn-blue" style="left:525px;top:2641px;width:151px;height:36px">Contact Us Today</a>

<svg class="abs" style="left:0;top:2735px" width="1200" height="442" viewBox="0 0 1200 442" aria-hidden="true">
  <path d="M0 20C60 50 120 60 220 50C380 35 470 -10 640 5C800 20 860 70 1000 50C1100 36 1160 20 1200 45V442H0Z" fill="var(--accent)"/>
  <path d="M0 35C60 62 120 70 220 60C380 45 470 5 640 18C800 32 860 80 1000 62C1100 50 1160 38 1200 58V442H0Z" fill="var(--black)"/>
</svg>
<div class="abs brand" style="left:62px;top:2880px;color:var(--white);font-size:26px;line-height:1.15">Brightfold Laundry<br>Company</div>
<p class="abs" style="left:62px;top:2940px;width:250px;font-size:12px;line-height:21px;color:var(--white)">We are proud to offer high quality and convenient services to the area residents and business owners and strive to keep our customers' clothing in tip top shape.</p>
<div class="abs footer-col" style="left:338px;top:2884px"><h4>Site Map</h4><ul><li>Home</li><li>About</li><li>Services</li><li>Why Choose Us</li><li>Blog</li><li>Contact Us</li></ul></div>
<div class="abs footer-col" style="left:614px;top:2884px;width:250px">
  <h4>Contact Us</h4>
  <div class="contact-row"><svg width="16" height="18" viewBox="0 0 16 18"><path d="M8 1a5 5 0 0 1 5 5c0 4-5 9-5 9S3 10 3 6a5 5 0 0 1 5-5z" fill="#fff"/><circle cx="8" cy="6" r="2" fill="#000"/></svg><span>Lorem Ipsum is simply dummy text of the.</span></div>
  <div class="contact-row"><svg width="16" height="16" viewBox="0 0 24 24"><path d="M6.6 10.8a15 15 0 0 0 6.6 6.6l2.2-2.2c.3-.3.7-.4 1-.2 1.1.4 2.3.6 3.6.6.6 0 1 .4 1 1V20c0 .6-.4 1-1 1A17 17 0 0 1 3 4c0-.6.4-1 1-1h3.5c.6 0 1 .4 1 1 0 1.3.2 2.5.6 3.6.1.3 0 .7-.2 1z" fill="#fff"/></svg><span style="font-weight:500">404-555-0142</span></div>
  <div class="contact-row"><svg width="18" height="13" viewBox="0 0 18 13"><rect width="18" height="13" fill="#fff"/><path d="M0 0l9 7 9-7" stroke="#000" fill="none"/></svg><span>info@brightfoldlaundry.example</span></div>
</div>
<div class="abs footer-col" style="left:890px;top:2884px"><h4>Social Media</h4>
  <div style="display:flex;gap:18px">
    <div class="social" style="border:1px solid var(--white)"></div>
    <div class="social" style="background:var(--white)"></div>
    <div class="social" style="background:var(--white)"></div>
  </div>
</div>
<div class="abs" style="left:0;top:3139px;width:1200px;height:38px;background:var(--primary);color:var(--white);font-size:12px;display:flex;align-items:center;justify-content:center">&copy; Copyright 2022&nbsp;<b style="font-weight:500">Brightfold Laundry</b>.All Right Reserved.</div>

</body>
</html>
```